Business Stationary for 4713 Radio Communications Company
Business Cards, Letterhead, Continuation Paper and Email Signature
Business Stationary for 4713 Radio Communications Company - Telecommunications
Creative Brief
Use same font as used in my logo
or as website (Rokkit)
Cutting-Edge
Gareth Pellow
Director
Fernway Business Centre Linford Close Andover Hampshire RG27 8QN United Kingdom
gareth@4713.co.uk
www.4713.co.uk
Please design letterhead using following additional info: VAT No: 384 9017 63 Company Registration No: 07192648 Continuation paper to have just logo design. Email signatures for both gareth pellow (gareth@4713.co.uk) and melora pellow (melora@4713.co.uk)
twitter.com/4713ltd facebook.com/4713limited

```html
<!DOCTYPE html>
<html lang="en">
<head>
<meta charset="utf-8">
<title>4713 Radio Communications Company – Stationery</title>
<link rel="stylesheet" href="https://fonts.googleapis.com/css2?family=Sorts+Mill+Goudy&display=swap">
<style>
  :root {
    --bg: #4a4a4a;
    --paper: #ffffff;
    --red: #990000;
    --dark: #333333;
    --ink: #3a3a3a;
    --rose: #cc7a7a;
    --rose-soft: #dca3a3;
    --grey: #a0a0a0;
    --footer-text: #f2f2f2;
  }
  * { margin: 0; padding: 0; box-sizing: border-box; }
  html, body { width: 1200px; height: 836px; overflow: hidden; }
  body {
    position: relative;
    background: var(--bg);
    font-family: "Sorts Mill Goudy", "Goudy Bookletter 1911", serif;
    color: var(--ink);
  }
  .sprite { position: absolute; width: 0; height: 0; }
  .piece { position: absolute; background: var(--paper); overflow: hidden; }

  /* brand mark: plain circle + name */
  .brand { position: absolute; display: flex; align-items: center; gap: 4px; }
  .brand-dot { border-radius: 50%; background: var(--red); flex: none; }
  .brand-name { color: var(--dark); line-height: 1; }

  .pattern-band {
    position: absolute;
    background: linear-gradient(90deg, var(--rose) 0%, var(--rose-soft) 40%, var(--rose) 62%, var(--grey) 82%, #b4b4b4 100%);
  }

  /* business cards */
  .card { width: 217px; height: 124px; border-radius: 62px 0 0 62px; }
  .card-front-1 { left: 76px; top: 145px; }
  .card-front-2 { left: 76px; top: 277px; }
  .card .brand { left: 20px; top: 46px; }
  .card .brand-dot { width: 30px; height: 30px; }
  .card .brand-name { font-size: 20px; }
  .card-details { position: absolute; left: 136px; top: 25px; font-size: 5px; line-height: 6px; }
  .card-name { color: var(--red); font-size: 7px; line-height: 8px; }
  .card-address { margin-top: 6px; }
  .card-contacts { margin-top: 5px; list-style: none; line-height: 6.35px; }
  .card-contacts li, .sig-contacts li, .lh-contacts li { display: flex; align-items: center; }
  .card-contacts svg { width: 4px; height: 4px; margin-right: 4px; fill: var(--red); flex: none; }

  .card-back { left: 321px; top: 277px; width: 217px; height: 124px; background: var(--red); border-radius: 0 62px 62px 0; }
  .card-back-band { position: absolute; left: 0; top: 49px; width: 203px; height: 25px; background: var(--paper); border-radius: 0 12.5px 12.5px 0; overflow: hidden; }
  .card-back-band .pattern-band { left: 0; top: 0; width: 164px; height: 25px; }
  .card-back-band .brand { left: 167px; top: 8px; gap: 2px; }
  .card-back-band .brand-dot { width: 8px; height: 8px; }
  .card-back-band .brand-name { font-size: 9px; }
  .card-back-url { position: absolute; left: 0; width: 217px; top: 99px; text-align: center; color: #f0dada; font-size: 5px; letter-spacing: 3px; }

  /* email signatures */
  .signature { left: 108px; width: 398px; height: 152px; }
  .signature-1 { top: 441px; }
  .signature-2 { top: 612px; }
  .signature .brand { left: 22px; top: 38px; gap: 5px; }
  .signature .brand-dot { width: 36px; height: 36px; }
  .signature .brand-name { font-size: 24px; }
  .sig-person { position: absolute; left: 96px; width: 214px; top: 42px; padding-right: 0; }
  .sig-name { color: var(--red); font-size: 15px; line-height: 16px; width: 104px; text-align: left; }
  .signature-2 .sig-name { margin-left: -8px; }
  .sig-role { font-size: 10px; line-height: 13px; }
  .signature-2 .sig-role { margin-left: -8px; }
  .sig-divider { position: absolute; top: 44px; width: 1px; height: 32px; background: var(--ink); }
  .sig-divider-a { left: 210px; }
  .sig-divider-b { left: 309px; }
  .sig-address { position: absolute; left: 220px; top: 44px; font-size: 7px; line-height: 8.4px; }
  .sig-contacts { position: absolute; left: 321px; top: 44px; font-size: 7px; line-height: 8.4px; list-style: none; }
  .sig-contacts svg { width: 6px; height: 6px; margin-right: 3px; fill: var(--red); flex: none; }
  .sig-band { position: absolute; left: 0; top: 110px; width: 398px; height: 31px; }
  .band-red { position: absolute; left: 0; top: 0; height: 100%; background: var(--red); }
  .band-dark { position: absolute; top: 0; height: 100%; background: var(--dark); }
  .sig-band .band-red { width: 35px; }
  .sig-band .pattern-band { left: 35px; top: 0; width: 194px; height: 31px; }
  .sig-band .band-dark { left: 229px; width: 169px; }

  /* letterhead */
  .letterhead { left: 569px; top: 70px; width: 527px; height: 683px; }
  .letterhead .brand { left: 30px; top: 44px; gap: 5px; }
  .letterhead .brand-dot { width: 32px; height: 32px; }
  .letterhead .brand-name { font-size: 22px; }
  .lh-footer-band { position: absolute; left: 0; top: 629px; width: 527px; height: 38px; }
  .lh-footer-band .band-red { width: 47px; }
  .lh-footer-band .pattern-band { left: 47px; top: 0; width: 245px; height: 38px; }
  .lh-footer-band .band-dark { left: 292px; width: 235px; }
  .lh-address { position: absolute; left: 312px; top: 3px; font-size: 7px; line-height: 8.4px; color: var(--footer-text); }
  .lh-divider { position: absolute; left: 397px; top: 3px; width: 1px; height: 33px; background: var(--footer-text); }
  .lh-contacts { position: absolute; left: 405px; top: 3px; font-size: 7px; line-height: 8.4px; color: var(--footer-text); list-style: none; }
  .lh-contacts svg { width: 5px; height: 5px; margin-right: 3px; fill: var(--red); flex: none; }
  .lh-legal { position: absolute; left: 312px; top: 670px; font-size: 7px; line-height: 8px; color: var(--ink); white-space: nowrap; }
  .lh-legal .sep { margin: 0 5px; }
</style>
</head>
<body>

<svg class="sprite" aria-hidden="true">
  <defs>
    <symbol id="i-phone" viewBox="0 0 10 10"><path d="M0 4 Q5 0 10 4 L8.5 5 L7 4 L7 3 Q5 2.4 3 3 L3 4 L1.5 5 Z"/><rect x="2" y="5" width="6" height="4" rx="1"/></symbol>
    <symbol id="i-mobile" viewBox="0 0 10 10"><path d="M2.5 0 H7.5 V10 H2.5 Z M3.3 1 V8 H6.7 V1 Z"/></symbol>
    <symbol id="i-mail" viewBox="0 0 10 10"><path d="M0 2 H10 V8 H0 Z M0.8 2.6 L5 6 L9.2 2.6 Z" fill-rule="evenodd"/></symbol>
    <symbol id="i-web" viewBox="0 0 10 10"><path d="M5 0 A5 5 0 1 0 5.01 0 Z M5 1 A4 4 0 1 1 4.99 1 Z M4.5 0.5 H5.5 V9.5 H4.5 Z M0.5 4.5 H9.5 V5.5 H0.5 Z" fill-rule="evenodd"/></symbol>
    <symbol id="i-square" viewBox="0 0 10 10"><rect x="0.5" y="0.5" width="9" height="9" rx="1"/></symbol>
  </defs>
</svg>

<!-- Business card front: Melora -->
<section class="piece card card-front-1">
  <div class="brand"><span class="brand-dot"></span><span class="brand-name">4713</span></div>
  <div class="card-details">
    <p class="card-name">Melora Pellow</p>
    <p>Director</p>
    <p class="card-address">Fernway Business Centre<br>Linford Close, Andover<br>Hampshire, RG27 8QN<br>United Kingdom</p>
    <ul class="card-contacts">
      <li><svg><use href="#i-phone"/></svg>01632 960412</li>
      <li><svg><use href="#i-mobile"/></svg>07700 900318</li>
      <li><svg><use href="#i-mail"/></svg>melora@4713.co.uk</li>
      <li><svg><use href="#i-web"/></svg>www.4713.co.uk</li>
      <li><svg><use href="#i-square"/></svg>4713</li>
      <li><svg><use href="#i-square"/></svg>4713</li>
    </ul>
  </div>
</section>

<!-- Business card front: Gareth -->
<section class="piece card card-front-2">
  <div class="brand"><span class="brand-dot"></span><span class="brand-name">4713</span></div>
  <div class="card-details">
    <p class="card-name">Gareth Pellow</p>
    <p>Director</p>
    <p class="card-address">Fernway Business Centre<br>Linford Close, Andover<br>Hampshire, RG27 8QN<br>United Kingdom</p>
    <ul class="card-contacts">
      <li><svg><use href="#i-phone"/></svg>01632 960412</li>
      <li><svg><use href="#i-mobile"/></svg>07700 900742</li>
      <li><svg><use href="#i-mail"/></svg>gareth@4713.co.uk</li>
      <li><svg><use href="#i-web"/></svg>www.4713.co.uk</li>
      <li><svg><use href="#i-square"/></svg>4713</li>
      <li><svg><use href="#i-square"/></svg>4713</li>
    </ul>
  </div>
</section>

<!-- Business card back -->
<section class="piece card-back">
  <div class="card-back-band">
    <div class="pattern-band" role="img" aria-label="Large brand numerals pattern in rose and grey"></div>
    <div class="brand"><span class="brand-dot"></span><span class="brand-name">4713</span></div>
  </div>
  <p class="card-back-url">www.4713.co.uk</p>
</section>

<!-- Email signature: Gareth -->
<section class="piece signature signature-1">
  <div class="brand"><span class="brand-dot"></span><span class="brand-name">4713</span></div>
  <div class="sig-person" style="left:124px;">
    <p class="sig-name">Gareth Pellow</p>
    <p class="sig-role">Director</p>
  </div>
  <span class="sig-divider sig-divider-a"></span>
  <p class="sig-address">Fernway Business Centre<br>Linford Close, Andover<br>Hampshire, RG27 8QN<br>United Kingdom</p>
  <span class="sig-divider sig-divider-b"></span>
  <ul class="sig-contacts">
    <li><svg><use href="#i-phone"/></svg>01632 960412</li>
    <li><svg><use href="#i-mobile"/></svg>07700 900742</li>
    <li><svg><use href="#i-mail"/></svg>gareth@4713.co.uk</li>
    <li><svg><use href="#i-web"/></svg>www.4713.co.uk</li>
  </ul>
  <div class="sig-band">
    <span class="band-red"></span>
    <div class="pattern-band" role="img" aria-label="Large brand numerals pattern in rose and grey"></div>
    <span class="band-dark"></span>
  </div>
</section>

<!-- Email signature: Melora -->
<section class="piece signature signature-2">
  <div class="brand"><span class="brand-dot"></span><span class="brand-name">4713</span></div>
  <div class="sig-person" style="left:126px;">
    <p class="sig-name">Melora Pellow</p>
    <p class="sig-role">Director</p>
  </div>
  <span class="sig-divider sig-divider-a"></span>
  <p class="sig-address">Fernway Business Centre<br>Linford Close, Andover<br>Hampshire, RG27 8QN<br>United Kingdom</p>
  <span class="sig-divider sig-divider-b"></span>
  <ul class="sig-contacts">
    <li><svg><use href="#i-phone"/></svg>01632 960412</li>
    <li><svg><use href="#i-mobile"/></svg>07700 900318</li>
    <li><svg><use href="#i-mail"/></svg>melora@4713.co.uk</li>
    <li><svg><use href="#i-web"/></svg>www.4713.co.uk</li>
  </ul>
  <div class="sig-band">
    <span class="band-red"></span>
    <div class="pattern-band" role="img" aria-label="Large brand numerals pattern in rose and grey"></div>
    <span class="band-dark"></span>
  </div>
</section>

<!-- Letterhead -->
<section class="piece letterhead">
  <div class="brand"><span class="brand-dot"></span><span class="brand-name">4713</span></div>
  <div class="lh-footer-band">
    <span class="band-red"></span>
    <div class="pattern-band" role="img" aria-label="Large brand numerals pattern in rose and grey"></div>
    <span class="band-dark"></span>
    <p class="lh-address">Fernway Business Centre<br>Linford Close, Andover<br>Hampshire, RG27 8QN<br>United Kingdom</p>
    <span class="lh-divider"></span>
    <ul class="lh-contacts">
      <li><svg><use href="#i-phone"/></svg>01632 960412</li>
      <li><svg><use href="#i-mobile"/></svg>07700 900742</li>
      <li><svg><use href="#i-mail"/></svg>info@4713.co.uk</li>
      <li><svg><use href="#i-web"/></svg>www.4713.co.uk</li>
    </ul>
  </div>
  <p class="lh-legal">VAT No: 384 9017 63<span class="sep">|</span>Company Registration No: 07192648</p>
</section>

</body>
</html>
```